Postcard Design

We need a postcard design size DL, front and back in colour, for a Excavation and Earthmoving company specialising in residential jobs including landscaping, drainage, pool excavations and fill ins, footings, trenching, driveways, retaining walls and after build clean ups
using images from out plazafolio page https://www.plazafolio.example/4926038175314807/photos/pb.4926038175314807.-3318640000.2550117792./4718329840636279/?type=3&theater

```html
<!DOCTYPE html>
<html lang="en">
<head>
<meta charset="utf-8">
<title>Digger Dan Groundworks – DL Postcard</title>
<link href="https://fonts.googleapis.com/css2?family=Lato:ital,wght@0,700;0,900;1,400&family=Oswald:wght@500&display=swap" rel="stylesheet">
<style>
  :root {
    --green: #3cb519;
    --green-dark: #2f9412;
    --charcoal: #2b2b2b;
    --charcoal-light: #4a4a4a;
    --panel-light: #f2f2f2;
    --panel-mid: #d9d9d9;
    --white: #ffffff;
    --ink: #3a3a3a;
    --backdrop: #ece9e4;
  }
  * { box-sizing: border-box; margin: 0; padding: 0; }
  html, body { width: 825px; height: 1200px; overflow: hidden; }
  body { background: var(--backdrop); font-family: "Lato", Arial, sans-serif; position: relative; }

  .postcard {
    position: absolute; left: 70px; width: 687px; height: 324px;
    background: var(--green); overflow: hidden;
    box-shadow: 0 3px 10px rgba(0,0,0,.25);
  }
  .postcard--front { top: 236px; }
  .postcard--back { top: 628px; }

  .layer { position: absolute; left: 0; top: 0; width: 687px; height: 324px; }
  .photo { position: absolute; }

  /* ---------- front ---------- */
  .front__hero {
    clip-path: polygon(0 0, 300px 0, 357px 176px, 0 176px);
    background: linear-gradient(180deg, #b9c0c6 0%, #d7d2c7 45%, #a58e72 75%, #7d6a55 100%);
  }
  .front__services-panel {
    clip-path: polygon(0 184px, 360px 184px, 396px 294px, 0 294px);
    background: linear-gradient(180deg, var(--charcoal-light), var(--charcoal));
  }
  .front__brand-panel {
    clip-path: polygon(322px 12px, 687px 12px, 687px 294px, 413px 294px);
    background: linear-gradient(180deg, var(--panel-light), var(--panel-mid) 55%, var(--panel-light));
  }

  .services {
    position: absolute; top: 196px; left: 18px;
    display: grid; grid-template-columns: 172px 180px; row-gap: 2px;
    list-style: none; color: var(--white);
    font-style: italic; font-weight: 400; font-size: 16px; line-height: 18.5px;
  }
  .services li::before {
    content: ""; display: inline-block; width: 5px; height: 5px; border-radius: 50%;
    background: var(--green); margin: 0 10px 3px 0; vertical-align: middle;
  }

  .brand {
    position: absolute; display: flex; align-items: center; gap: 10px;
    color: var(--green); font-weight: 900; line-height: 1;
  }
  .brand__dot { border-radius: 50%; background: var(--green); flex: none; }
  .brand--front { left: 396px; top: 22px; font-size: 31px; }
  .brand--front .brand__dot { width: 22px; height: 22px; }
  .brand--back { left: 24px; top: 24px; font-size: 19px; }
  .brand--back .brand__dot { width: 14px; height: 14px; }

  .photo-frame {
    position: absolute; border: 2px solid var(--green); background: var(--white);
    padding: 3px; display: flex; gap: 3px;
  }
  .front__gallery { left: 407px; top: 120px; width: 258px; height: 103px; }
  .front__gallery .photo { position: static; flex: 1; }
  .photo--loader { background: linear-gradient(180deg, #8fb46a, #5d7f3e 60%, #3a3a2e); }
  .photo--truck { background: linear-gradient(180deg, #7a8f5c, #c9c6bf 55%, #6c5a44); }

  .tagline {
    position: absolute; left: 412px; top: 242px; width: 268px; text-align: center;
    font-weight: 900; font-size: 17px; line-height: 21px; text-transform: uppercase;
  }
  .tagline__first { color: var(--ink); display: block; }
  .tagline__second { color: var(--green); display: block; }

  .call-badge {
    position: absolute; width: 96px; height: 96px; border-radius: 50%;
    background: var(--white); border: 5px solid var(--green);
    box-shadow: 0 0 0 3px var(--white);
    display: flex; align-items: center; justify-content: center; text-align: center;
    font-family: "Oswald", "Arial Narrow", sans-serif; font-weight: 500;
    font-size: 19px; line-height: 22px; color: var(--ink); text-transform: uppercase;
  }
  .call-badge span { color: var(--green); display: block; }
  .postcard--front .call-badge { left: 293px; top: 121px; }
  .postcard--back .call-badge { left: 293px; top: 101px; }

  /* ---------- back ---------- */
  .back__brand-panel {
    clip-path: polygon(0 0, 352px 0, 370px 104px, 0 104px);
    background: linear-gradient(180deg, var(--panel-light), var(--panel-mid));
  }
  .back__access-frame { left: 188px; top: 13px; width: 160px; height: 80px; }
  .back__access-frame .photo { position: static; flex: 1; }
  .photo--access { background: linear-gradient(90deg, #e6e6e6 30%, #b57b52 60%, #caa27c); }

  .back__retaining {
    clip-path: polygon(364px 0, 687px 0, 687px 138px, 384px 138px);
    background: linear-gradient(180deg, #9fae88, #6e5a40 55%, #8c9a5e);
  }
  .back__truck {
    clip-path: polygon(334px 156px, 687px 156px, 687px 294px, 322px 294px);
    background: linear-gradient(180deg, #a9b59a, #e8e8e6 45%, #cfcfcc 75%, #5d5d55);
  }
  .back__site-one { left: 0; top: 110px; width: 168px; height: 86px; background: linear-gradient(180deg, #b7c2c8, #9d8a70 60%, #6e5842); }
  .back__site-two { left: 172px; top: 110px; width: 132px; height: 86px; clip-path: polygon(0 0, 128px 0, 132px 86px, 0 86px); background: linear-gradient(180deg, #7f9a63, #8a6c4d 60%, #5e7a45); }

  .back__contact-panel {
    clip-path: polygon(0 204px, 336px 204px, 322px 294px, 0 294px);
    background: linear-gradient(180deg, var(--charcoal-light), var(--charcoal));
  }
  .contact-heading {
    position: absolute; left: 22px; top: 218px;
    font-family: "Oswald", "Arial Narrow", sans-serif; font-weight: 500;
    font-size: 25px; line-height: 30px; color: var(--white); text-transform: uppercase;
  }
  .contact-list {
    position: absolute; left: 115px; top: 214px; list-style: none;
    font-family: "Oswald", "Arial Narrow", sans-serif; font-weight: 500;
    font-size: 17px; line-height: 22px; color: var(--white);
  }
  .contact-list .contact-name { color: var(--green); text-transform: uppercase; }
  .contact-web { font-family: "Lato", Arial, sans-serif; font-weight: 400; font-size: 15px; }
</style>
</head>
<body>

<section class="postcard postcard--front" aria-label="Postcard front">
  <div class="layer photo front__hero" role="img" aria-label="Photo of an orange mini excavator working beside a new brick house"></div>
  <div class="layer front__services-panel"></div>
  <div class="layer front__brand-panel"></div>

  <ul class="services">
    <li>Landscaping</li><li>Trenching</li>
    <li>Drainage</li><li>Driveways</li>
    <li>Pool excavations</li><li>Retaining walls</li>
    <li>Fill ins &amp; footings</li><li>After build clean ups</li>
  </ul>

  <div class="brand brand--front"><span>Digger Dan<br>Groundworks</span><span class="brand__dot"></span></div>

  <div class="photo-frame front__gallery">
    <div class="photo photo--loader" role="img" aria-label="Photo of a tracked skid steer loader on grass"></div>
    <div class="photo photo--truck" role="img" aria-label="Photo of the company tip truck carrying a mini excavator"></div>
  </div>

  <p class="tagline">
    <span class="tagline__first">We can't move heaven</span>
    <span class="tagline__second">Butwe can move earth</span>
  </p>

  <div class="call-badge"><p>Call us<span>today!</span></p></div>
</section>

<section class="postcard postcard--back" aria-label="Postcard back">
  <div class="layer back__brand-panel"></div>
  <div class="layer photo back__retaining" role="img" aria-label="Photo of a worker with a mini excavator building a timber retaining wall"></div>
  <div class="layer photo back__truck" role="img" aria-label="Photo of the company tip truck with sign-written side panels"></div>
  <div class="photo back__site-one" role="img" aria-label="Photo of a mini excavator moving soil on a building site"></div>
  <div class="photo back__site-two" role="img" aria-label="Photo of a mini excavator removing a tree stump"></div>
  <div class="layer back__contact-panel"></div>

  <div class="brand brand--back"><span>Digger Dan<br>Groundworks</span><span class="brand__dot"></span></div>

  <div class="photo-frame back__access-frame">
    <div class="photo photo--access" role="img" aria-label="Photo of a mini excavator in a narrow side access beside a brick wall"></div>
  </div>

  <p class="contact-heading">Contact<br>us now!</p>
  <ul class="contact-list">
    <li><span class="contact-name">Callum</span> : 0400111222</li>
    <li><span class="contact-name">Rory</span> : 0400333444</li>
    <li class="contact-web">diggerdangroundworks.example</li>
  </ul>

  <div class="call-badge"><p>Call us<span>today!</span></p></div>
</section>

</body>
</html>
```